Playful Website Design Needed Pet Sitting and Dog Walking Business

Need a simple one page Web Design Built on WordPress.
Sections:

About Us
Services Provided
Costs
Contact Us
Intake Form (Questionnaire that goes to email)
See us in Action

Industry/Entity Type

Pet Sitting and Dog Walking

Number of Pages Required

1 page

Font styles to use
Other font styles liked:
• See the Business Card Font and use that.

Colors
EE7325
F08F49
F5BC92
FAE3D3
FDF4ED

Requirements
Must have
• See attached Logo Design, with Font's and Colors Use these as theme guide

```html
<!DOCTYPE html>
<html lang="en">
<head>
<meta charset="utf-8">
<title>Paw Haven Lodge – Overnight Pet Boarding</title>
<link href="https://fonts.googleapis.com/css2?family=Lexend:wght@400;500;600&family=Questrial&family=Oswald:wght@500&family=Caveat:wght@600&display=swap" rel="stylesheet">
<style>
:root{
  --orange:#EE7325;
  --orange-soft:#F08F49;
  --peach:#F5BC92;
  --cream:#FAE3D3;
  --ink:#222222;
  --muted:#555555;
  --brown:#7a3e0c;
  --green:#5a9a1a;
  --forest:#1f4b22;
  --mauve:#d8c3cf;
  --blush:#ecdfe5;
  --panel:#f5f5f5;
}
*{box-sizing:border-box;margin:0;padding:0}
html,body{width:1200px;height:4261px;overflow:hidden}
body{background:var(--orange);font-family:"Questrial",sans-serif;color:var(--ink);position:relative}
.page{position:absolute;left:0;top:665px;width:1200px;height:2930px;background:#fff;overflow:hidden}
.abs{position:absolute}
.brand{font-family:"Questrial",sans-serif;color:var(--orange);font-size:22px;display:flex;align-items:center;gap:8px;white-space:nowrap}
.brand .dot{width:14px;height:14px;border-radius:50%;background:var(--orange);flex:none}
.pill{border-radius:40px;color:#fff;font-family:"Lexend",sans-serif;font-weight:500;display:flex;align-items:center;justify-content:center;letter-spacing:.5px;white-space:nowrap}
.pill-green{background:var(--green)}
.pill-brown{background:var(--brown)}
.hero-photo{left:466px;top:0;width:734px;height:577px;background:linear-gradient(120deg,#e8e2dc 0%,#c9b9a6 40%,#6f7a52 60%,#b9a89a 100%)}
.hero-title{left:161px;top:160px;width:400px;font-family:"Lexend",sans-serif;font-weight:500;font-size:42px;line-height:46px;color:var(--ink)}
.hero-sub{left:161px;top:320px;width:330px;font-size:16px;line-height:24px;color:var(--muted)}
.form-card{left:749px;top:513px;width:287px;height:367px;background:#fff;box-shadow:0 4px 18px rgba(0,0,0,.15);padding:28px 22px}
.form-card h3{font-family:"Lexend",sans-serif;font-weight:500;font-size:16px;text-align:center;white-space:nowrap}
.form-card p{font-size:10px;line-height:14px;text-align:center;margin-top:8px;color:var(--muted)}
.field{height:26px;border:1px solid #ddd;border-radius:3px;margin-top:12px;font-size:8px;color:#888;padding:8px;display:flex;justify-content:space-between}
.form-card .submit{width:120px;height:28px;margin:18px auto 0;font-size:10px}
.about-title{left:161px;top:640px;width:520px;font-family:"Lexend",sans-serif;font-weight:500;font-size:19px;line-height:27px}
.script{font-family:"Caveat",cursive;color:var(--brown);font-size:24px}
.about-text{left:161px;top:745px;width:520px;font-size:10.5px;line-height:21px;color:var(--muted)}
.gallery div{position:absolute}
.center-title{width:1200px;text-align:center;font-family:"Lexend",sans-serif;font-weight:500;font-size:19px}
.price-band{top:1554px;height:334px;width:1200px}
.price-left{left:0;width:600px;height:334px;background:var(--mauve)}
.price-right{left:600px;width:600px;height:334px;background:var(--blush)}
.price h4{font-family:"Lexend",sans-serif;font-weight:500;font-size:22px}
.price .amt{font-family:"Oswald",sans-serif;font-size:40px;margin-top:12px;color:#2b2b2b;white-space:nowrap}
.price .per{font-size:11px;text-align:right;width:250px;margin-top:-4px}
.price .note{font-family:"Lexend",sans-serif;font-size:16px;line-height:22px;margin-top:18px}
.amenities{top:1888px;left:0;width:1200px;height:558px;background:var(--panel)}
.card{position:absolute;width:172px;background:#fff;box-shadow:0 2px 8px rgba(0,0,0,.05);padding:30px 26px}
.card .ico{width:42px;height:42px;border-radius:50%;background:#e4e4e4;display:flex;align-items:center;justify-content:center}
.card p{font-size:10px;line-height:15px;color:#666;margin-top:14px}
.map{top:2446px;left:0;width:1200px;height:298px;background:linear-gradient(90deg,#e7e9ec 0%,#e2e6e3 60%,#9ec1ea 72%,#a8c9ee 100%)}
.map-card{left:233px;top:2470px;width:180px;height:247px;background:#fff;box-shadow:0 2px 10px rgba(0,0,0,.2);text-align:center;padding:16px 10px}
.map-card h5{font-family:"Lexend",sans-serif;font-size:10px;font-weight:600;margin-top:10px}
.map-card .addr{font-size:9px;color:#777;line-height:12px;margin-top:4px}
.map-card .tel{font-family:"Lexend",sans-serif;font-size:12px;font-weight:500;margin-top:10px;display:flex;justify-content:center;gap:5px;align-items:center}
.footer{top:2744px;left:0;width:1200px;height:186px;background:var(--forest);color:#fff}
.footer h6{font-family:"Lexend",sans-serif;font-weight:500;font-size:11px;letter-spacing:.5px}
.footer .small{font-size:9px;line-height:13px;margin-top:10px;color:#e6e6e6}
.footer .big{font-family:"Lexend",sans-serif;font-size:16px;margin-top:10px}
.copy{left:0;width:1200px;top:160px;text-align:center;font-size:8px;color:#cfd8cf}
</style>
</head>
<body>
<main class="page">

  <section class="hero">
    <div class="abs hero-photo" role="img" aria-label="Photo of a smiling woman feeding a treat to a beagle in a living room"></div>
    <div class="abs brand" style="left:31px;top:26px"><span class="dot"></span>Paw Haven Lodge</div>
    <div class="abs pill pill-green" style="left:1033px;top:37px;width:137px;height:27px;font-size:8px">BOOK NOW - CALL US</div>
    <h1 class="abs hero-title">You Won't Be the<br>Only One on<br>Vacation</h1>
    <p class="abs hero-sub">We're the perfect home away from home for your dog when they need an overnight stay.</p>
    <div class="abs pill pill-brown" style="left:161px;top:423px;width:166px;height:37px;font-size:9px">BOOK YOUR STAY&nbsp;
      <svg width="12" height="11" viewBox="0 0 12 11"><circle cx="6" cy="7.5" r="3" fill="#fff"/><circle cx="2" cy="4" r="1.4" fill="#fff"/><circle cx="10" cy="4" r="1.4" fill="#fff"/><circle cx="4.3" cy="1.6" r="1.3" fill="#fff"/><circle cx="7.7" cy="1.6" r="1.3" fill="#fff"/></svg>
    </div>
  </section>

  <form class="abs form-card">
    <h3>CALL +1 (555) 014-2368</h3>
    <p>Or fill out this form and we'll contact you shortly to arrange your dog an overnight stay.</p>
    <div class="field">Name</div>
    <div class="field">Email</div>
    <div class="field">Phone</div>
    <div class="field"><span>How Many Pets?</span><span>⌄</span></div>
    <div class="field"><span>Desired Dates of Stay</span><span>▦</span></div>
    <div class="pill pill-green submit">SUBMIT</div>
  </form>

  <section class="about">
    <h2 class="abs about-title">You want peace of mind while you're away from your pup. They'll get the <span class="script">personalized care</span> and accommodations they deserve.</h2>
    <p class="abs about-text">At Paw Haven Lodge, we offer an intimate, safe, and cozy boarding facility and daycare for pets of Maple Bay. Your cat or dog will enjoy loads of individual attention with plenty of comfortable amenities in spacious suites that will make them feel right at home.</p>
    <div class="abs" style="left:0;top:855px;width:278px;height:100px;background:linear-gradient(90deg,#e9dcc8,#c9a77c);border-radius:0 50px 50px 0" role="img" aria-label="Photo of sleeping golden puppies"></div>
    <div class="abs" style="left:717px;top:809px;width:73px;height:101px;background:linear-gradient(#f6c531,#ee7325 60%,#6aa338);border-radius:36px 36px 8px 8px" role="img" aria-label="Cartoon flower mascot illustration"></div>
  </section>

  <section class="gallery">
    <div style="left:159px;top:985px;width:295px;height:441px;background:linear-gradient(160deg,#8aa3a8,#b48a5f 55%,#c9c7bf)" role="img" aria-label="Photo of a beagle running in an outdoor pen"></div>
    <div style="left:460px;top:985px;width:292px;height:174px;background:linear-gradient(#b8cde0,#5d8a3b)" role="img" aria-label="Photo of a grassy fenced yard"></div>
    <div style="left:460px;top:1165px;width:292px;height:261px;background:linear-gradient(#4f7a3c,#9c9c98)" role="img" aria-label="Photo of a chain-link dog run"></div>
    <div style="left:760px;top:985px;width:276px;height:234px;background:linear-gradient(135deg,#e9e6df,#b8b1a5)" role="img" aria-label="Photo of white boarding suites"></div>
    <div style="left:760px;top:1225px;width:276px;height:201px;background:linear-gradient(135deg,#d9d4ca,#8e7a64 60%,#3b5ea8)" role="img" aria-label="Photo of a cat resting in a suite"></div>
  </section>

  <h2 class="abs center-title" style="top:1505px">With simple pricing for the whole family</h2>

  <section class="abs price-band">
    <div class="abs price-left"></div>
    <div class="abs price-right"></div>
    <div class="abs price" style="left:249px;top:62px">
      <h4>DOGS:</h4>
      <div class="amt">$35.00 - $40.00</div>
      <div class="per">per night</div>
      <div class="note">Discount On Additional Pets<br>Sharing Same Room</div>
    </div>
    <div class="abs price" style="left:631px;top:62px">
      <h4>CATS:</h4>
      <div class="amt">$20.00 - $23.00</div>
      <div class="per">per night</div>
      <div class="note">Discount On Additional Pets<br>Sharing Same Room</div>
    </div>
  </section>
  <div class="abs" style="left:0;top:1686px;width:154px;height:256px;background:linear-gradient(#cfc9c4,#3a3434);border-radius:40px 40px 10px 10px" role="img" aria-label="Photo of a French bulldog puppy"></div>
  <div class="abs" style="left:988px;top:1686px;width:212px;height:202px;background:linear-gradient(#b9b4ad,#5e5a55);border-radius:60px 60px 0 0" role="img" aria-label="Photo of a tabby cat looking up"></div>

  <section class="abs amenities">
    <h2 class="abs center-title" style="top:79px">Amenities Include</h2>
    <div class="card" style="left:234px;top:129px;height:144px"><div class="ico"><svg width="20" height="20" viewBox="0 0 20 20"><path d="M2 10 L10 3 L18 10 V18 H2Z" fill="#4a2c2c"/></svg></div><p>Spacious suites for dogs and cats</p></div>
    <div class="card" style="left:421px;top:129px;height:144px"><div class="ico"><svg width="20" height="20" viewBox="0 0 20 20"><path d="M10 2 C6 8 5 11 5 13 A5 5 0 0 0 15 13 C15 11 14 8 10 2Z" fill="#4a2c2c"/></svg></div><p>Fresh water</p></div>
    <div class="card" style="left:608px;top:129px;height:144px"><div class="ico"><svg width="20" height="20" viewBox="0 0 20 20"><path d="M3 9 H17 L15 17 H5Z" fill="#4a2c2c"/><circle cx="10" cy="6" r="3" fill="#4a2c2c"/></svg></div><p>Low-residue diet (or you can provide your pet's food from home)</p></div>
    <div class="card" style="left:795px;top:129px;height:144px"><div class="ico"><svg width="20" height="20" viewBox="0 0 20 20"><circle cx="7" cy="3.5" r="2" fill="#4a2c2c"/><path d="M6 6 L9 6 L10 12 L12 18 H10 L8 13 L5 18 H3 L6 11Z" fill="#4a2c2c"/><rect x="12" y="13" width="6" height="3" fill="#4a2c2c"/></svg></div><p>5 walks daily for dogs</p></div>
    <div class="card" style="left:327px;top:293px;height:150px"><div class="ico"><svg width="20" height="20" viewBox="0 0 20 20"><circle cx="9" cy="4" r="2" fill="#4a2c2c"/><path d="M7 7 H11 V13 L13 18 H11 L9 14 L7 18 H5 L7 12Z" fill="#4a2c2c"/><circle cx="16" cy="10" r="2" fill="#4a2c2c"/></svg></div><p>Individual playtime</p></div>
    <div class="card" style="left:514px;top:293px;height:150px"><div class="ico"><svg width="20" height="20" viewBox="0 0 20 20"><rect x="2" y="11" width="16" height="5" fill="#4a2c2c"/><rect x="3" y="7" width="5" height="4" fill="#4a2c2c"/></svg></div><p>Comfortable bedding washed daily or as needed</p></div>
    <div class="card" style="left:701px;top:293px;height:150px"><div class="ico"><svg width="20" height="20" viewBox="0 0 20 20"><path d="M8 3 H12 V8 H17 V12 H12 V17 H8 V12 H3 V8 H8Z" fill="#4a2c2c"/></svg></div><p>Medications administered if needed by trained staff</p></div>
  </section>

  <section class="abs map" role="img" aria-label="Street map showing the boarding location by the bay"></section>
  <div class="abs map-card">
    <div class="brand" style="justify-content:center;font-size:15px"><span class="dot" style="width:10px;height:10px"></span>Paw Haven Lodge</div>
    <svg width="16" height="20" viewBox="0 0 16 20" style="margin-top:8px"><path d="M8 1 A6 6 0 0 1 14 7 C14 12 8 19 8 19 C8 19 2 12 2 7 A6 6 0 0 1 8 1Z" fill="none" stroke="#555" stroke-width="1.5"/><circle cx="8" cy="7" r="2" fill="#555"/></svg>
    <h5>Conveniently Located</h5>
    <p class="addr">Your Bussiness Address<br>goes here, okay</p>
    <div class="tel"><svg width="11" height="11" viewBox="0 0 12 12"><path d="M2 1 L4.5 1 L5.5 4 L4 5 C5 7 6 8 7 8.5 L8 7 L11 8 V10.5 C11 11 10.5 11 10 11 C5 11 1 7 1 2 C1 1.5 1.5 1 2 1Z" fill="#222"/></svg>(555) 014-2368</div>
    <div class="pill pill-green" style="width:120px;height:26px;font-size:9px;margin:14px auto 0">BOOK YOUR STAY</div>
  </div>

  <footer class="abs footer">
    <div class="abs" style="left:205px;top:50px"><h6>Visit Us:</h6><p class="small">Monday - Friday: 7:00 am - 6:00 pm<br>Saturday: 8:00 am - 12:00 pm<br>Sunday: Closed</p></div>
    <div class="abs" style="left:455px;top:50px"><h6>Find Us:</h6><p class="small">Your Bussiness Address<br>goes here, okay</p></div>
    <div class="abs" style="left:680px;top:50px"><h6>Book Now - Call Us:</h6><p class="big">(555) 014-2368</p></div>
    <div class="abs brand" style="left:905px;top:60px;font-size:17px"><span class="dot" style="width:11px;height:11px"></span>Paw Haven Lodge</div>
    <p class="abs copy">Copyright © 2023 paw-haven-lodge. All rights reserved.</p>
  </footer>

</main>
</body>
</html>
```